Business card for an e-commerce/social networking website
Bazorin
Simple
Yousef Karim AlShehhi
Chief Financial Officer
Palm Crest Isle, Orchid Court Apt 418 Abu Dhabi, United Arab Emirates
1-800-BAZORIN
alshehhi@bazorin.ae
www.Bazorin.ae
the card be contemporary. easy on the eye. not cluttered.
the single "B" in the box.

```html
<!DOCTYPE html>
<html lang="en">
<head>
<meta charset="utf-8">
<title>Bazorin Business Card</title>
<link href="https://fonts.googleapis.com/css2?family=Open+Sans:wght@400;600;700&display=swap" rel="stylesheet">
<style>
:root{
  --bg:#e6e7e9;
  --card:#ffffff;
  --blue:#1a8ad4;
  --blue-dark:#0d6fb3;
  --blue-light:#8cc6ee;
  --ink:#5a5f66;
  --muted:#8a9097;
  --rule:#d5d9de;
}
*{margin:0;padding:0;box-sizing:border-box}
html,body{width:1200px;height:864px;overflow:hidden;background:var(--bg);font-family:'Open Sans',Arial,sans-serif}
.stage{position:relative;width:1200px;height:864px}
.card{position:absolute;top:277px;width:540px;height:310px;background:var(--card);border-radius:22px;box-shadow:0 12px 30px rgba(0,0,0,.18);overflow:hidden}
.card--front{left:40px}
.card--back{left:620px}

/* front */
.front-mark{position:absolute;left:222px;top:92px;width:96px;height:96px;border-radius:14px;background:var(--blue);display:flex;align-items:center;justify-content:center;color:#fff;font-weight:700;font-size:62px;box-shadow:0 4px 10px rgba(0,0,0,.15)}
.front-url{position:absolute;left:0;right:0;top:222px;text-align:center;color:var(--ink);font-size:11px;letter-spacing:6px}

/* back */
.brand{position:absolute;left:34px;top:62px;width:220px;height:62px;border:1px solid var(--rule);border-radius:6px;display:flex;align-items:center;gap:10px;padding-left:16px;box-shadow:0 3px 8px rgba(0,0,0,.1)}
.brand-square{width:30px;height:30px;border-radius:6px;background:var(--blue)}
.brand-name{color:var(--blue);font-weight:700;font-size:32px;line-height:1}
.person{position:absolute;left:34px;top:142px;width:220px;text-align:center}
.person-name{color:var(--blue);font-weight:600;font-size:14px}
.person-title{color:var(--muted);font-size:11px;margin-top:2px}
.address{position:absolute;left:34px;top:196px;width:230px;color:var(--ink);font-size:10.5px;line-height:1.5;text-align:center}
.divider{position:absolute;left:280px;top:56px;width:1px;height:150px;background:var(--rule)}
.contacts{position:absolute;left:296px;top:56px;list-style:none}
.contacts li{display:flex;align-items:center;gap:8px;height:23px;color:var(--ink);font-size:11px}
.contacts svg{width:14px;height:14px;flex:none}
.wave{position:absolute;left:0;bottom:0;width:540px;height:140px}
</style>
</head>
<body>
<main class="stage">
  <section class="card card--front">
    <div class="front-mark">B</div>
    <p class="front-url">www.Bazorin.ae</p>
  </section>

  <section class="card card--back">
    <div class="brand">
      <span class="brand-square"></span>
      <span class="brand-name">Bazorin</span>
    </div>
    <div class="person">
      <p class="person-name">Yousef Karim AlShehhi</p>
      <p class="person-title">Chief Financial Officer</p>
    </div>
    <p class="address">Palm Crest Isle, Orchid Court Apt 418<br>Abu Dhabi, United Arab Emirates</p>
    <span class="divider"></span>
    <ul class="contacts">
      <li><svg viewBox="0 0 14 14"><circle cx="7" cy="7" r="7" fill="#1a8ad4"/><path d="M4.5 3.5h1.6l.7 2-1 .8a5 5 0 0 0 2 2l.8-1 2 .7v1.6c0 .5-.4.9-.9.9A6.3 6.3 0 0 1 3.6 4.4c0-.5.4-.9.9-.9z" fill="#fff"/></svg>1-800-BAZORIN</li>
      <li><svg viewBox="0 0 14 14"><circle cx="7" cy="7" r="7" fill="#1a8ad4"/><rect x="5" y="3" width="4" height="8" rx="1" fill="#fff"/></svg>+971-50-417-293-6</li>
      <li><svg viewBox="0 0 14 14"><circle cx="7" cy="7" r="7" fill="#1a8ad4"/><path d="M4.5 3.5h1.6l.7 2-1 .8a5 5 0 0 0 2 2l.8-1 2 .7v1.6c0 .5-.4.9-.9.9A6.3 6.3 0 0 1 3.6 4.4c0-.5.4-.9.9-.9z" fill="#fff"/></svg>0552-318-904</li>
      <li><svg viewBox="0 0 14 14"><circle cx="7" cy="7" r="7" fill="#1a8ad4"/><rect x="4" y="5" width="6" height="5" fill="#fff"/><rect x="5" y="3" width="4" height="2" fill="#fff"/></svg>02-631-472-80</li>
      <li><svg viewBox="0 0 14 14"><circle cx="7" cy="7" r="7" fill="#1a8ad4"/><rect x="3.5" y="4.5" width="7" height="5" fill="#fff"/><path d="M3.5 4.5 7 7.5l3.5-3" stroke="#1a8ad4" fill="none" stroke-width=".8"/></svg>alshehhi@bazorin.ae</li>
      <li><svg viewBox="0 0 14 14"><circle cx="7" cy="7" r="7" fill="#1a8ad4"/><circle cx="7" cy="7" r="3.5" fill="none" stroke="#fff" stroke-width="1"/><path d="M3.5 7h7M7 3.5v7" stroke="#fff" stroke-width=".8"/></svg>www.Bazorin.ae</li>
    </ul>
    <svg class="wave" viewBox="0 0 540 140" preserveAspectRatio="none" aria-hidden="true">
      <path d="M180 140 C300 120 420 70 540 20 V140 Z" fill="var(--blue-light)"/>
      <path d="M230 140 C340 125 440 85 540 45 V140 Z" fill="var(--blue)"/>
      <path d="M330 140 C420 130 480 110 540 85 V140 Z" fill="var(--blue-dark)"/>
    </svg>
  </section>
</main>
</body>
</html>
```